tax advisory service business cards
Professional
Loretta Fenwick
Tax Advisory Specialist
51924 HOLLISTER LANE SUITE C
PRAIRIEVILL, LA 70812
FISCAL9COUNSELDESK@QUILLMAIL.COM
FCD4FILE.COM

```html
<!DOCTYPE html>
<html lang="en">
<head>
<meta charset="utf-8">
<title>Fenwick Fiscal Counsel – Business Cards</title>
<link rel="stylesheet" href="https://fonts.googleapis.com/css2?family=Libre+Baskerville:wght@700&family=Roboto:wght@400;500;700&display=swap">
<style>
  :root {
    --page-bg: #e4e2df;
    --card-white: #ffffff;
    --band-black: #0d0d0f;
    --gold: #d9a92a;
    --gold-light: #f1cf63;
    --navy: #1f2b5c;
    --grey: #8a8a8a;
    --ink: #1b1b1b;
    --contact: #f3f3f3;
  }
  * { box-sizing: border-box; margin: 0; padding: 0; }
  html, body { width: 1200px; height: 751px; overflow: hidden; }
  body {
    background: var(--page-bg);
    position: relative;
    font-family: "Roboto", Arial, sans-serif;
  }
  .card {
    position: absolute;
    width: 540px;
    height: 320px;
    background: var(--card-white);
    border-radius: 14px;
    overflow: hidden;
    box-shadow: 0 8px 24px rgba(0,0,0,0.18);
  }
  .card--front { left: 45px; top: 215px; }
  .card--back { left: 615px; top: 215px; }

  .card__bands { position: absolute; inset: 0; width: 100%; height: 100%; }

  .brand-dot {
    position: absolute;
    left: 64px; top: 44px;
    width: 44px; height: 44px;
    border-radius: 50%;
    background: var(--navy);
  }
  .company {
    position: absolute;
    font-family: "Libre Baskerville", Georgia, serif;
    font-weight: 700;
    color: var(--ink);
    letter-spacing: 0.2px;
    white-space: nowrap;
  }
  .company--front { left: 24px; top: 112px; font-size: 13px; }
  .tagline {
    position: absolute;
    font-size: 7px;
    color: var(--ink);
    border-top: 1px solid var(--ink);
    padding-top: 2px;
    white-space: nowrap;
  }
  .tagline--front { left: 30px; top: 132px; }

  .holder { position: absolute; left: 300px; top: 42px; }
  .holder__name { font-size: 20px; font-weight: 700; color: var(--navy); }
  .holder__title { font-size: 10px; color: var(--grey); margin-top: 2px; }

  .contact {
    position: absolute;
    left: 300px; top: 176px;
    list-style: none;
    color: var(--contact);
    font-size: 10px;
    line-height: 14px;
  }
  .contact__item { display: flex; align-items: center; gap: 5px; white-space: nowrap; }
  .contact__gap { margin-top: 8px; }
  .contact__icon { width: 9px; height: 9px; fill: var(--contact); flex: none; }

  .company--back { right: 26px; bottom: 46px; font-size: 13px; }
  .tagline--back { right: 32px; bottom: 34px; }
</style>
</head>
<body>

<section class="card card--front" aria-label="Business card front">
  <svg class="card__bands" viewBox="0 0 540 320" preserveAspectRatio="none" aria-hidden="true">
    <defs>
      <linearGradient id="goldSweep" x1="0" y1="0" x2="1" y2="0">
        <stop offset="0" stop-color="#d9a92a"/>
        <stop offset="0.5" stop-color="#f1cf63"/>
        <stop offset="1" stop-color="#c8951c"/>
      </linearGradient>
    </defs>
    <path d="M0 200 C150 225 300 118 540 130 L540 142 C300 130 150 238 0 214 Z" fill="url(#goldSweep)"/>
    <path d="M0 214 C150 238 300 130 540 142 L540 262 C380 240 200 300 0 262 Z" fill="#0d0d0f"/>
    <path d="M0 262 C200 300 380 240 540 262 L540 270 C380 250 200 314 0 280 Z" fill="url(#goldSweep)"/>
  </svg>

  <div class="brand-dot" aria-hidden="true"></div>
  <p class="company company--front">FENWICK FISCAL COUNSEL, INC.</p>
  <p class="tagline tagline--front">Guiding Your Taxes the Right Way</p>

  <div class="holder">
    <p class="holder__name">Loretta Fenwick</p>
    <p class="holder__title">Tax Advisory Specialist</p>
  </div>

  <ul class="contact">
    <li class="contact__item">51924 HOLLISTER LANE SUITE C</li>
    <li class="contact__item">Prairieville, LA 70812</li>
    <li class="contact__item contact__gap">
      <svg class="contact__icon" viewBox="0 0 10 10"><path d="M2 0h2l1 3-1.5 1a6 6 0 0 0 2.5 2.5L7 5l3 1v2a2 2 0 0 1-2 2A8 8 0 0 1 0 2a2 2 0 0 1 2-2z"/></svg>
      225-555-0148
    </li>
    <li class="contact__item">
      <svg class="contact__icon" viewBox="0 0 10 10"><path d="M0 2h10v6H0z M0 2l5 3.5L10 2" stroke="#0d0d0f" stroke-width="0.8"/></svg>
      FISCAL9COUNSELDESK@QUILLMAIL.COM
    </li>
    <li class="contact__item">
      <svg class="contact__icon" viewBox="0 0 10 10"><circle cx="5" cy="5" r="5"/></svg>
      WWW.FCD4FILE.COM
    </li>
  </ul>
</section>

<section class="card card--back" aria-label="Business card back">
  <p class="company company--back">FENWICK FISCAL COUNSEL, INC.</p>
  <p class="tagline tagline--back">Guiding Your Taxes the Right Way</p>
</section>

</body>
</html>
```